Harbourlight Dental Centre Kelvale business cards and presentation folder

dental practice needing innovative black business cards for 2 different dentists witrh appointment details written at the back of the card for the patient.
name of dentists: Dr Anjali R Venkatesan B.D.S., M.P.H (Melb)
Dr. Raj Kalpat B.D.S.

Target Market(s)

professioinal, working class

Industry/Entity Type

Dental Clinic

Contact Information for Business Card

Dr. Raj Kalpat B.D.S.

Font styles to use
Sans Serif

Requirements
Must have
• Front side: logo
• dentist name
• phone number: 07- 5918 2243
• back side: appointment details: date, time,
• Address: 117C, 58 Tarrow Street, Kelvale - 4561, Queensland
• Email: admin@harbourlightdentalkelvale.example.au
• Website: www.harbourlightdental.example.au
• preferable logo colors
Nice to have
• classy look more pleasing

```html
<!DOCTYPE html>
<html lang="en">
<head>
<meta charset="utf-8">
<title>Harbourlight Dental Centre Kelvale – Business Card</title>
<link rel="stylesheet" href="https://fonts.googleapis.com/css2?family=Questrial&display=swap">
<style>
  :root {
    --backdrop: #d9d9d9;
    --card: #1a1718;
    --accent: #9fc17f;
    --band-text: #1b1a1a;
    --soft-grey: #a7a9ac;
  }
  * { box-sizing: border-box; margin: 0; padding: 0; }
  html, body { width: 1200px; height: 1200px; overflow: hidden; }
  body {
    background: var(--backdrop);
    font-family: "Questrial", "Century Gothic", sans-serif;
    position: relative;
  }
  .card {
    position: absolute;
    left: 240px;
    width: 720px;
    height: 435px;
    background: var(--card);
    box-shadow: 0 18px 30px rgba(0,0,0,0.35);
  }
  .card--front { top: 106px; }
  .card--back { top: 630px; }

  .name-band {
    position: absolute;
    left: 0; right: 0;
    top: 38px;
    height: 58px;
    background: var(--accent);
    padding: 4px 0 0 17px;
    color: var(--band-text);
    font-size: 21px;
    line-height: 25px;
    letter-spacing: 0.2px;
  }

  .contact-list {
    position: absolute;
    left: 20px;
    top: 244px;
    list-style: none;
    color: var(--accent);
    font-size: 14px;
    line-height: 16px;
  }
  .contact-list li {
    display: flex;
    align-items: flex-start;
    margin-bottom: 12px;
  }
  .contact-list svg {
    width: 18px; height: 18px;
    flex: none;
    margin-right: 14px;
    fill: var(--accent);
  }

  .brand {
    position: absolute;
    display: flex;
    align-items: center;
    color: var(--accent);
    text-transform: uppercase;
  }
  .brand__dot {
    flex: none;
    border-radius: 50%;
    background: var(--accent);
  }
  .brand__name { line-height: 1.15; letter-spacing: 1px; }

  .brand--small { right: 20px; top: 270px; gap: 10px; }
  .brand--small .brand__dot { width: 14px; height: 14px; }
  .brand--small .brand__name { font-size: 15px; }

  .brand--large { left: 0; right: 0; top: 170px; justify-content: center; gap: 18px; }
  .brand--large .brand__dot { width: 30px; height: 30px; }
  .brand--large .brand__name { font-size: 31px; }
</style>
</head>
<body>

<section class="card card--front">
  <div class="name-band">
    <p>Dr Anjali R Venkatesan B.D.S., M.P.H (Melb)</p>
    <p>Dr. Raj Kalpat B.D.S.</p>
  </div>

  <ul class="contact-list">
    <li>
      <svg viewBox="0 0 24 24" aria-hidden="true"><path d="M6.6 10.8a15.1 15.1 0 0 0 6.6 6.6l2.2-2.2a1 1 0 0 1 1-.25 11.4 11.4 0 0 0 3.6.57 1 1 0 0 1 1 1V20a1 1 0 0 1-1 1A17 17 0 0 1 3 4a1 1 0 0 1 1-1h3.5a1 1 0 0 1 1 1c0 1.25.2 2.45.57 3.57a1 1 0 0 1-.25 1z"/></svg>
      <span>07- 5918 2243</span>
    </li>
    <li>
      <svg viewBox="0 0 24 24" aria-hidden="true"><path d="M3 8l9-5 9 5v11H3z M3 8l9 6 9-6" fill="none" stroke="#9fc17f" stroke-width="2"/></svg>
      <span>admin@harbourlightdentalkelvale.example.au</span>
    </li>
    <li>
      <svg viewBox="0 0 24 24" aria-hidden="true"><g fill="none" stroke="#9fc17f" stroke-width="1.8"><circle cx="12" cy="12" r="9"/><ellipse cx="12" cy="12" rx="4" ry="9"/><path d="M3 12h18M5 7h14M5 17h14"/></g></svg>
      <span>www.harbourlightdental.example.au</span>
    </li>
    <li>
      <svg viewBox="0 0 24 24" aria-hidden="true"><path d="M2 11l10-7 10 7v1h-2v9H4v-9H2z M9 21v-6h6v6" fill="none" stroke="#9fc17f" stroke-width="1.8"/></svg>
      <span>117C, 58 Tarrow Street, Kelvale<br>4561, QUEENSLAND</span>
    </li>
  </ul>

  <div class="brand brand--small">
    <span class="brand__dot"></span>
    <span class="brand__name">Harbourlight Dental<br>Centre Kelvale</span>
  </div>
</section>

<section class="card card--back">
  <div class="brand brand--large">
    <span class="brand__dot"></span>
    <span class="brand__name">Harbourlight Dental<br>Centre Kelvale</span>
  </div>
</section>

</body>
</html>
```